Pre-workout label and Super Greens label for Vantora Nutrition Supplements

I need a label design for Club Vantora's 2 supplements. The first is a Pre-workout. The Pre-workout label needs to be 11.25 x 2.5 inches. This label will go on a black container. The second is a Super-Green. The Super-Green label should be 11.25 x 4.25 inches and will go on a white container. We have been selling these for a few years but the current labels are a little meh. I'd like something trendier and bolder. Must keep the Club Vantora branding. All the nurtition data must appear . I attached the current designs so you can know the flavors, nutrtional data etc. Thank you!
Updates

I can upload the Club Vantora logo! If anyone can tell me how to do that.

```html
<!DOCTYPE html>
<html lang="en">
<head>
<meta charset="utf-8">
<title>Vantora Nutrition – Pre-Workout and Super Greens Labels</title>
<link rel="stylesheet" href="https://fonts.googleapis.com/css2?family=Barlow+Condensed:wght@400;500&family=Roboto:ital,wght@0,400;0,700;1,700;1,900&family=Michroma&display=swap">
<style>
  :root {
    --page: #ffffff;
    --blue-deep: #2a7cc2;
    --blue-light: #62c6ea;
    --frame-pink: #d6248f;
    --ink: #111418;
    --ink-navy: #0d2a4a;
    --white: #ffffff;
    --accent-red: #e5232c;
    --silver-dark: #9a9ea3;
    --silver-light: #f4f4f5;
  }
  * { box-sizing: border-box; margin: 0; padding: 0; }
  html, body { width: 1200px; height: 441px; overflow: hidden; background: var(--page); }
  body { position: relative; font-family: "Roboto", Arial, sans-serif; color: var(--ink); }

  .label { position: absolute; }

  /* ---------- Pre-Workout ---------- */
  .preworkout {
    left: 105px; top: 124px; width: 547px; height: 151px;
    border-radius: 4px;
    background: linear-gradient(180deg, var(--blue-deep) 0%, #3aa3d8 30%, var(--blue-light) 100%);
  }
  .preworkout .frame {
    position: absolute; left: 24px; top: 21px; width: 494px; height: 110px;
    border: 1px solid var(--frame-pink); border-radius: 4px;
  }
  .pw-directions {
    position: absolute; left: 36px; top: 30px; width: 113px; height: 75px;
    border: 1px solid var(--ink-navy); border-radius: 6px;
    padding: 4px 5px; color: var(--white); font-size: 3.1px; line-height: 1.45;
  }
  .pw-directions h3 { font-size: 4.2px; font-weight: 700; display: inline; }
  .pw-directions .lead { font-size: 3.3px; font-weight: 700; }
  .pw-directions p { margin-top: 2px; }
  .pw-disclaimer {
    position: absolute; left: 36px; top: 110px; width: 66px; height: 14px;
    border: 1px solid var(--ink-navy); border-radius: 7px;
    color: var(--white); font-size: 2.4px; line-height: 1.3; text-align: center; padding: 2px 4px;
  }
  .pw-center { position: absolute; left: 173px; top: 30px; width: 200px; text-align: center; }
  .brand-mark {
    display: block; margin: 0 auto; width: 14px; height: 14px;
    background: var(--accent-red); border-radius: 2px;
  }
  .brand-name {
    font-family: "Barlow Condensed", sans-serif; font-weight: 400; letter-spacing: 0.5px;
  }
  .pw-center .brand-name { font-size: 7.5px; color: var(--ink-navy); margin-top: 4px; }
  .pw-center .product { font-style: italic; font-weight: 700; font-size: 8.5px; color: var(--ink); margin-top: 1px; }
  .pw-center .flavor {
    font-family: "Michroma", sans-serif; font-size: 6px; letter-spacing: 1.2px;
    color: var(--white); margin-top: 5px;
  }
  .pw-benefits { display: flex; justify-content: center; gap: 14px; margin-top: 4px; }
  .pw-benefit { width: 36px; color: var(--white); font-size: 3px; line-height: 1.3; }
  .pw-benefit .icon {
    display: block; margin: 3px auto 0; width: 17px; height: 17px;
    border-radius: 50%; background: var(--ink);
  }
  .pw-center .dietary { font-style: italic; font-weight: 900; font-size: 8.3px; color: var(--ink); margin-top: 4px; }
  .pw-center .servings { font-weight: 700; font-size: 3.6px; color: var(--ink); margin-top: 1px; }

  .facts { background: var(--white); border: 0.8px solid var(--ink); padding: 2px 2px; font-size: 2.5px; line-height: 1.35; }
  .facts h4 { font-size: 4.8px; font-weight: 700; line-height: 1.1; }
  .facts .head { border-bottom: 1.4px solid var(--ink); padding-bottom: 1px; }
  .facts .row { display: grid; grid-template-columns: 1fr 30px 12px; border-bottom: 0.4px solid #777; }
  .facts .row span:last-child { text-align: right; }
  .facts .foot { font-size: 2.3px; }

  .pw-facts { position: absolute; left: 385px; top: 28px; width: 126px; }
  .pw-other { position: absolute; left: 386px; top: 107px; width: 124px; color: var(--white); font-size: 2.4px; line-height: 1.5; opacity: 0.9; }
  .pw-other p + p { margin-top: 3px; }

  /* ---------- Super Greens ---------- */
  .greens {
    left: 676px; top: 120px; width: 489px; height: 187px; border-radius: 6px;
    background: linear-gradient(90deg, var(--silver-dark) 0%, var(--silver-light) 40%, var(--silver-light) 60%, var(--silver-dark) 100%);
  }
  .sg-panel {
    position: absolute; left: 11px; top: 14px; width: 102px; height: 162px;
    background: var(--white); border-radius: 6px; padding: 12px 7px; font-size: 3.1px; line-height: 1.45;
  }
  .sg-panel h3 { display: inline; font-size: 4.4px; font-weight: 700; }
  .sg-panel .caution { margin-top: 28px; }
  .sg-panel .fda { position: absolute; left: 7px; bottom: 9px; width: 82px; font-size: 2.5px; }
  .sg-center { position: absolute; left: 140px; top: 20px; width: 210px; text-align: center; }
  .sg-center .brand-mark { width: 22px; height: 22px; }
  .sg-center .brand-name { font-size: 8.5px; color: var(--ink); margin-top: 10px; letter-spacing: 0.8px; }
  .sg-center .product { font-style: italic; font-weight: 700; font-size: 11px; color: var(--accent-red); margin-top: 12px; }
  .sg-center .flavor { font-family: "Michroma", sans-serif; font-size: 8px; letter-spacing: 1.4px; color: var(--ink); margin-top: 3px; }
  .sg-benefits { display: flex; justify-content: center; gap: 14px; margin-top: 8px; }
  .sg-benefit { width: 38px; font-weight: 700; font-size: 4px; line-height: 1.1; display: flex; flex-direction: column; align-items: center; }
  .sg-benefit .txt { height: 14px; display: flex; align-items: flex-end; }
  .sg-benefit .icon { margin-top: 3px; width: 25px; height: 25px; border-radius: 50%; background: var(--ink); display: flex; align-items: center; justify-content: center; }
  .sg-center .dietary {
    font-style: italic; font-weight: 900; font-size: 8.5px; margin: 8px auto 0; width: 108px;
    border-top: 0.6px solid #bbb; border-bottom: 0.6px solid #bbb; padding: 1px 0;
  }
  .sg-center .servings { font-weight: 700; font-size: 4.6px; margin-top: 6px; }
  .sg-facts { position: absolute; left: 359px; top: 14px; width: 112px; font-size: 2.2px; }
  .sg-facts .row { grid-template-columns: 1fr 18px 10px; }
  .sg-facts .blend { grid-template-columns: 1fr 14px 8px; padding: 1px 0; }
  .sg-other { position: absolute; left: 360px; top: 150px; width: 110px; font-size: 2.2px; line-height: 1.4; }
</style>
</head>
<body>

<section class="label preworkout" aria-label="Pre-Workout label">
  <div class="frame"></div>

  <div class="pw-directions">
    <h3>Directions:</h3> <span class="lead">Use on training days only. Mix 1 scoop with 6-8 oz of cold water 15-30 minutes prior to training.</span>
    <p>Warning: Not intended for use by persons under age 18. Do not exceed recommended dose. Do not combine with other sources of caffeine, including coffee, tea, soda or other stimulant products. Consult your physician prior to use if you are pregnant or nursing, or if you are taking any medication, including but not limited to MAOI inhibitors, antidepressants, aspirin, blood thinners or anti-inflammatory drugs. Consult your physician prior to use if you have a medical condition, including but not limited to heart, liver, kidney or thyroid disease, high blood pressure or glaucoma. Discontinue use 2 weeks prior to surgery or if you feel unwell.</p>
  </div>
  <div class="pw-disclaimer">*These statements have not been evaluated by the Food and Drug Administration. This product is not intended to diagnose, treat, cure or prevent any disease.</div>

  <div class="pw-center">
    <span class="brand-mark"></span>
    <div class="brand-name">VANTORA NUTRITION</div>
    <div class="product">Pre-Workout</div>
    <div class="flavor">WATERMELON SUGAR</div>
    <div class="pw-benefits">
      <div class="pw-benefit">(Caffeine)<br>ENERGY*<span class="icon" role="img" aria-label="Energy icon, runner"></span></div>
      <div class="pw-benefit">(Beta-alanine)<br>PERFORMANCE*<span class="icon" role="img" aria-label="Performance icon, athlete"></span></div>
      <div class="pw-benefit">(Creatine)<br>STRENGTH*<span class="icon" role="img" aria-label="Strength icon, flexed arm"></span></div>
    </div>
    <div class="dietary">Dietary Supplement</div>
    <div class="servings">30 SERVINGS 240g (8.5oz)</div>
  </div>

  <div class="facts pw-facts">
    <div class="head">
      <h4>Supplement Facts</h4>
      <div>Serving Size: 1 Scoop (8 g)</div>
      <div>Servings per Container: 30</div>
    </div>
    <div class="row"><span></span><span>Amount per Serving</span><span>%DV</span></div>
    <div class="row"><span>Vitamin C (as Ascorbic Acid)</span><span>250 mg</span><span>278%</span></div>
    <div class="row"><span>Vitamin B6 (as Pyridoxal-5-Phosphate)</span><span>0.035 mg</span><span>2%</span></div>
    <div class="row"><span>Folate</span><span>250 mcg DFE</span><span>63%</span></div>
    <div class="row"><span>Vitamin B12 (as Methylcobalamin)</span><span>20 mcg</span><span>833%</span></div>
    <div class="row"><span>Calcium (as Calcium Silicate)</span><span>18.38 mg</span><span>1%</span></div>
    <div class="row"><span>Beta-Alanine</span><span>1.5 g</span><span>†</span></div>
    <div class="row"><span>Creatine Monohydrate</span><span>1 g</span><span>†</span></div>
    <div class="row"><span>L-Arginine Alpha-Ketoglutarate</span><span>1 g</span><span>†</span></div>
    <div class="row"><span>L-Citrulline Malate</span><span>1 g</span><span>†</span></div>
    <div class="row"><span>N-Acetyl L-Tyrosine</span><span>500 mg</span><span>†</span></div>
    <div class="row"><span>Caffeine Anhydrous</span><span>250 mg</span><span>†</span></div>
    <div class="row"><span>Spirulina Extract</span><span>30 mg</span><span>†</span></div>
    <div class="foot">† Daily Value (DV) not established</div>
  </div>
  <div class="pw-other">
    <p>Other Ingredients: Citric Acid, Potassium, Malic Acid, Silicon Dioxide, Natural and Artificial Flavors, Acesulfame Potassium, Sucralose, and FD&amp;C Red #40.</p>
    <p>Distributed by: Club Vantora, 1200 Harbor Way, Suite 4, Springfield</p>
  </div>
</section>

<section class="label greens" aria-label="Super Greens label">
  <div class="sg-panel">
    <p><h3>Directions:</h3> Mix one (1) scoop into 6-8oz of your favorite non-citrus juice, water, smoothie, or protein shake.</p>
    <p class="caution"><h3>CAUTION:</h3> As with any dietary supplement, consult your healthcare practitioner before using this product, especially if you are pregnant, nursing, anticipate surgery, take medication on a regular basis or are otherwise under medical supervision. Store in a cool, dry place. Keep out of reach of children.</p>
    <p class="fda">*These statements have not been evaluated by the Food and Drug Administration. This product is not intended to diagnose, treat, cure or prevent any disease.</p>
  </div>

  <div class="sg-center">
    <span class="brand-mark"></span>
    <div class="brand-name">VANTORA NUTRITION</div>
    <div class="product">SUPER GREENS</div>
    <div class="flavor">APPLE CINNAMON</div>
    <div class="sg-benefits">
      <div class="sg-benefit"><span class="txt">DETOX<br>BODY*</span><span class="icon" role="img" aria-label="Detox icon, intestines"></span></div>
      <div class="sg-benefit"><span class="txt">PROMOTE<br>HEALTHY<br>DIGESTION*</span><span class="icon" role="img" aria-label="Digestion icon, stomach"></span></div>
      <div class="sg-benefit"><span class="txt">SUPPORT<br>IMMUNITY*</span><span class="icon" role="img" aria-label="Immunity icon, heart">
        <svg width="15" height="13" viewBox="0 0 24 21"><path d="M12 21 2.5 11.5A6 6 0 0 1 12 3.7a6 6 0 0 1 9.5 7.8Z" fill="#fff"/></svg>
      </span></div>
    </div>
    <div class="dietary">Dietary Supplement</div>
    <div class="servings">30 SERVINGS 240g (8.5oz)</div>
  </div>

  <div class="facts sg-facts">
    <div class="head">
      <h4>Supplement Facts</h4>
      <div>Serving Size: Approx. 1 Scoop (8 g)</div>
      <div>Servings per Container: 30</div>
    </div>
    <div class="row"><span></span><span>Amount</span><span>%DV</span></div>
    <div class="row"><span>Calories</span><span>40</span><span></span></div>
    <div class="row"><span>Total Fat</span><span>1.5 g</span><span>2%</span></div>
    <div class="row"><span>Total Carbohydrate</span><span>5 g</span><span>2%</span></div>
    <div class="row"><span>&nbsp;Dietary Fiber</span><span>2 g</span><span>7%</span></div>
    <div class="row"><span>&nbsp;Total Sugars</span><span>&lt;1 g</span><span></span></div>
    <div class="row"><span>Protein</span><span>2 g</span><span></span></div>
    <div class="row"><span>Vitamin E (as D-Alpha Tocopheryl)</span><span>40 mg</span><span>267%</span></div>
    <div class="row"><span>Calcium</span><span>30 mg</span><span>2%</span></div>
    <div class="row"><span>Iron</span><span>2.5 mg</span><span>14%</span></div>
    <div class="row"><span>Sodium</span><span>45 mg</span><span>1%</span></div>
    <div class="row"><span>Potassium</span><span>100 mg</span><span>2%</span></div>
    <div class="row blend"><span>Green Health Blend<br>Alfalfa Leaf, Barley Grass, Wheat Grass, Oat Grass, Spinach and Kale Powder</span><span>6.6 g</span><span>†</span></div>
    <div class="row blend"><span>Energy Blend<br>Beet Root, Maca Root and Green Tea Leaf Extract</span><span>1.41 g</span><span>†</span></div>
    <div class="row blend"><span>Detox Blend<br>Acerola Berry, Parsley Leaf, Milk Thistle Seed and Dandelion Root</span><span>420 mg</span><span>†</span></div>
    <div class="row blend"><span>Immunity Blend<br>Echinacea, Ginger Root and Grape Seed Extract</span><span>340 mg</span><span>†</span></div>
    <div class="row blend"><span>Probiotic Blend<br>L. acidophilus, B. bifidum, B. longum, S. thermophilus</span><span>150 mg</span><span>†</span></div>
    <div class="row blend"><span>Enzyme Blend<br>Amylase, Protease, Lipase, Lactase, Papain</span><span>120 mg</span><span>†</span></div>
    <div class="foot">Percent Daily Values based on a 2,000 calorie diet<br>† Daily Value (DV) not established</div>
  </div>
  <p class="sg-other">Other Ingredients: Organic Cinnamon Powder, Natural Flavor, Silicon Dioxide, Stevia Leaf Extract, Sucralose.</p>
</section>

</body>
</html>
```